Research Flier

I need to take a very bad flier that I made and turn it into an amazing flyer for my research group to be shared at a high profile conference.

```html
<!DOCTYPE html>
<html lang="en">
<head>
<meta charset="utf-8">
<title>Kindred Lab – Research Flier</title>
<link href="https://fonts.googleapis.com/css2?family=Poppins:wght@400;500;600;700&family=Oswald:wght@500&display=swap" rel="stylesheet">
<style>
:root{
  --backdrop:#d3d3d3;
  --paper:#ffffff;
  --orange:#df5528;
  --green:#b8dc8c;
  --green-text:#9fcf72;
  --ink:#2b2b2b;
  --soft:#f3f3f3;
}
*{margin:0;padding:0;box-sizing:border-box}
html,body{width:1200px;height:2400px;overflow:hidden}
body{background:var(--backdrop);font-family:"Poppins",sans-serif;color:var(--ink);position:relative}
.page{position:absolute;left:244px;width:764px;height:1080px;background:var(--paper);transform:scale(.932);transform-origin:0 0;overflow:hidden}
.page--front{top:138px}
.page--back{top:1255px}
.abs{position:absolute}

/* front */
.hero-photo{left:0;top:0;width:764px;height:350px;background:linear-gradient(135deg,#7a6a8e 0%,#c9b9a6 35%,#8a5a4a 60%,#5b4a52 100%)}
.hero-rule{left:0;top:348px;width:764px;height:4px;background:var(--orange)}
.brand-corner{left:390px;top:0;width:374px;height:160px}
.brand{left:485px;top:20px;display:flex;align-items:center;gap:8px}
.brand__dot{width:26px;height:26px;border-radius:50%;background:var(--orange)}
.brand__name{font-size:17px;font-weight:600;color:var(--ink);line-height:1.05;letter-spacing:.5px;width:140px}
.brand-divider{left:674px;top:18px;width:1px;height:44px;background:#6f8f5a}
.partner-badge{left:692px;top:22px;width:28px;height:28px;border-radius:50%;background:#5d7e46}

.pill{background:var(--green);border-radius:16px;font-weight:700;font-size:17px;color:#1e1e1e;padding:2px 11px;white-space:nowrap}
.label{color:var(--orange);font-weight:700;font-size:14px;line-height:1.3}
.mission-list{left:52px;top:468px;width:262px;list-style:none}
.mission-list li{display:flex;gap:12px;font-size:10.2px;line-height:1.22;margin-bottom:18px;text-align:justify;hyphens:auto;-webkit-hyphens:auto}
.mission-list .num{font-family:"Oswald",sans-serif;color:var(--orange);font-size:18px;line-height:1;min-width:18px}
.country{width:78px;font-size:5.6px;line-height:1.35;color:#555}
.country h4{font-size:10.5px;font-weight:600;color:var(--ink);border-bottom:1px solid #ddd;margin-bottom:3px;padding-bottom:1px}
.country ul{padding-left:7px}
.country--big{font-size:8px}

.goals{left:380px;top:485px;width:280px;list-style:none}
.goals li{position:relative;padding-left:16px;font-size:9.8px;line-height:1.2;margin-bottom:17px}
.goals li svg{position:absolute;left:0;top:1px}
.domain{width:160px}
.domain h5{color:var(--orange);font-size:9.6px;font-weight:600;line-height:1.15;padding-left:20px;position:relative;width:100px}
.domain h5 svg{position:absolute;left:0;top:-1px}
.domain p{font-size:9.6px;line-height:1.22;padding-left:21px;margin-top:6px;width:150px}
.sites{left:549px;top:903px;width:215px;height:177px;background:var(--green);padding:28px 17px}
.sites h3{font-size:15px;font-weight:700;margin-bottom:12px}
.sites p{font-size:9.4px;line-height:1.25;margin-bottom:10px}
.footer{left:0;top:1028px;width:420px;height:52px}
.footer__url{left:30px;top:1044px;display:flex;align-items:center;gap:6px;color:#fff;font-weight:600;font-size:12.5px}
.footer__url i{width:13px;height:13px;border-radius:50%;background:var(--green);display:block}
.front-rule{left:400px;top:1073px;width:150px;height:7px;background:var(--orange)}

/* back */
.back-head{left:0;top:0;width:764px;height:62px;background:var(--green);display:flex;align-items:center;justify-content:center;font-size:19.5px;font-weight:700;color:#1c1c1c}
.side-panel{left:0;top:62px;width:297px;height:970px;background:var(--soft)}
.h-orange{color:var(--orange);font-weight:700;font-size:20.5px;line-height:1.25}
.h-green{color:var(--green-text);font-weight:600;font-size:11.4px}
.body-text{font-size:9.8px;line-height:1.25}
.body-text--loose{line-height:1.85}
.placeholder{border-radius:4px}
.pub{left:315px;width:415px}
.pub h6{color:var(--green-text);font-size:9.5px;font-weight:600;margin-bottom:3px}
.pub p{font-size:9.6px;line-height:1.5}
.back-rule{left:395px;top:1070px;width:369px;height:10px;background:var(--orange)}
</style>
</head>
<body>

<!-- FRONT PAGE -->
<section class="page page--front">
  <div class="abs hero-photo" role="img" aria-label="Group photo of workshop participants holding training certificates"></div>
  <svg class="abs brand-corner" viewBox="0 0 374 160" aria-hidden="true">
    <path d="M0 0H374V145C300 110 180 100 90 55C50 35 20 15 0 0Z" fill="#b8dc8c"/>
    <path d="M374 145C300 110 180 100 90 55" fill="none" stroke="#df5528" stroke-width="3"/>
  </svg>
  <div class="abs brand"><span class="brand__dot"></span><span class="brand__name">OPEN HEART LEARNING</span></div>
  <div class="abs brand-divider"></div>
  <div class="abs partner-badge"></div>
  <div class="abs hero-rule"></div>

  <div class="abs pill" style="left:43px;top:385px">THE KINDRED LAB</div>
  <div class="abs label" style="left:54px;top:435px">MISSION :</div>
  <ol class="abs mission-list">
    <li><span class="num">01</span><span>Supporting the development of the evidence-based, Open Heart Learning program and CRCT for Educators by assessing program implementation and examining feasibility, impact, and long-term sustainability at the school, district, city, and national levels.</span></li>
    <li><span class="num">02</span><span>Developing effective tools and measures to CRCT and Open Heart Learning</span></li>
    <li style="margin-top:14px"><span class="num">03</span><span>Support global dissemination through impactful manualization</span></li>
    <li style="margin-top:22px"><span class="num">04</span><span>Contribute to compasson-based education studies worldwide through scientific advancements that examine compassion, common humanity, wellbeing, interdependence, and secular ethics.</span></li>
  </ol>

  <div class="abs country" style="left:55px;top:760px"><h4>USA</h4><ul><li>Several Studies of Late Elementary and Middle</li><li>Multiple School Districts</li><li>Implementation, RCT, Quasi-experimental, Qualitative, and Mixed Methods</li></ul></div>
  <div class="abs country" style="left:133px;top:760px"><h4>Sweden</h4><ul><li>Late Elementary</li><li>2 Schools</li><li>Feasibility &amp; Qualitative Impact Study</li></ul></div>
  <div class="abs country" style="left:222px;top:760px"><h4>Spain</h4><ul><li>Late Elementary</li><li>Multiple Schools Across Two Regions</li><li>Implementation Study</li></ul></div>
  <div class="abs country" style="left:297px;top:760px"><h4>Ukraine</h4><ul><li>Teachers</li><li>Feasibility &amp; Qualitative Impact Study</li></ul></div>
  <div class="abs country country--big" style="left:140px;top:838px"><h4 style="line-height:1.1">South<br>Korea</h4><ul><li>Elementary</li><li>Implementation Study</li></ul></div>
  <div class="abs country" style="left:218px;top:845px"><h4>Mongolia</h4><ul><li>Late Elementary to High School</li><li>800 + Students</li><li>6 Schools</li><li>Implementation study</li></ul></div>
  <div class="abs country" style="left:293px;top:845px"><h4>Mexico</h4><ul><li>Pre-service Course Study</li><li>Feasibility and Preliminary Impact</li></ul></div>
  <div class="abs country" style="left:58px;top:928px"><h4>Columbia</h4><ul><li>Late Elementary</li><li>300+ students</li><li>Implementation Study</li><li>Feasibility &amp; Qualitative Impact Study</li></ul></div>
  <div class="abs country" style="left:136px;top:928px"><h4>Brazil</h4><ul><li>Late Elementary</li><li>Ten Schools</li><li>Randomized Controlled Trial</li><li>Teachers &amp; Students</li></ul></div>
  <div class="abs country" style="left:214px;top:928px"><h4>Kenya</h4><ul><li>Late Elementary</li><li>2 Schools</li><li>Feasibility &amp; Qualitative Impact Study</li></ul></div>
  <div class="abs country" style="left:292px;top:928px"><h4>India</h4><ul><li>Late Elementary</li><li>More than 1300 Students</li><li>Urban and Rural Implementation studies</li><li>Case Studies</li></ul></div>

  <div class="abs pill" style="left:370px;top:380px">BUILDING FOR CHANGE</div>
  <div class="abs label" style="left:379px;top:432px">TO MEANINGFULLY IMPACT<br>CHANGE, WE HAVE :</div>
  <ul class="abs goals">
    <li><svg width="10" height="10" viewBox="0 0 10 10"><circle cx="5" cy="5" r="4.3" fill="none" stroke="#df5528"/><path d="M3 5l1.5 1.5L7 3.5" fill="none" stroke="#df5528"/></svg>IDentified seven critical domains for whole-school implementation sustainment</li>
    <li><svg width="10" height="10" viewBox="0 0 10 10"><circle cx="5" cy="5" r="4.3" fill="none" stroke="#df5528"/><path d="M3 5l1.5 1.5L7 3.5" fill="none" stroke="#df5528"/></svg>Conducted studies on sustainable implementation and its impact on compassionate systems</li>
    <li><svg width="10" height="10" viewBox="0 0 10 10"><circle cx="5" cy="5" r="4.3" fill="none" stroke="#df5528"/><path d="M3 5l1.5 1.5L7 3.5" fill="none" stroke="#df5528"/></svg>Begun work on global implementation frameworks, monitoring guides, and whole-school trainings</li>
  </ul>

  <div class="abs domain" style="left:381px;top:630px"><h5><svg width="16" height="16" viewBox="0 0 16 16"><circle cx="8" cy="8" r="6.5" fill="none" stroke="#df5528"/></svg>Leadership<br>Development</h5><p style="padding-left:22px">Those is leadership need skill and Open Heart understanding for implementation to thrive</p></div>
  <div class="abs domain" style="left:381px;top:727px"><h5><svg width="16" height="16" viewBox="0 0 16 16"><rect x="2" y="2" width="12" height="12" rx="2" fill="none" stroke="#df5528"/></svg>Student Voice</h5><p style="padding-left:22px">Empowering students to actively participate in and contribute to the SEL process strengthens the school community and supports SEL sustainability</p></div>
  <div class="abs domain" style="left:381px;top:838px"><h5><svg width="16" height="16" viewBox="0 0 16 16"><circle cx="8" cy="8" r="6.5" fill="none" stroke="#df5528"/></svg>Community<br>Engagement</h5><p style="padding-left:22px">Engaging families and communities creates a shared vision that enhances sustainability.</p></div>
  <div class="abs domain" style="left:381px;top:940px"><h5><svg width="16" height="16" viewBox="0 0 16 16"><circle cx="8" cy="8" r="6.5" fill="none" stroke="#df5528"/></svg>Communities<br>of Practice</h5><p style="padding-left:22px">Ongoing professional development creates opportunities and spaces to strengthen educator development.</p></div>
  <div class="abs domain" style="left:560px;top:632px"><h5><svg width="16" height="16" viewBox="0 0 16 16"><circle cx="8" cy="8" r="6.5" fill="none" stroke="#df5528"/></svg>Implementation</h5><p style="margin-top:4px">Sustainable practices involves strategies that embed SEL into the educational landscape of the school</p></div>
  <div class="abs domain" style="left:560px;top:714px"><h5><svg width="16" height="16" viewBox="0 0 16 16"><rect x="2" y="2" width="12" height="12" rx="2" fill="none" stroke="#df5528"/></svg>District Initiative<br>Alignment</h5><p style="margin-top:4px">Open Heart must align with school initiatives as a part of shared goals that are communicated.</p></div>
  <div class="abs domain" style="left:560px;top:815px"><h5><svg width="16" height="16" viewBox="0 0 16 16"><rect x="2" y="2" width="12" height="12" rx="2" fill="none" stroke="#df5528"/></svg>Adult SEL</h5><p style="margin-top:6px">Professional development includes SEL for adults to create supportive schools.</p></div>

  <div class="abs sites">
    <h3>RESEARCH SITES</h3>
    <p>We collaborate with global affiliates to conduct collaborative region-specific research.</p>
    <p>Read below to discover the impactful projects from our worldwide network!</p>
  </div>
  <svg class="abs footer" viewBox="0 0 420 52" aria-hidden="true"><path d="M0 0H360L410 52H0Z" fill="#df5528"/></svg>
  <div class="abs front-rule"></div>
  <div class="abs footer__url"><i></i>www.researchnotes.northfield.edu /kindredlab</div>
</section>

<!-- BACK PAGE -->
<section class="page page--back">
  <div class="abs back-head">Assessment Development Projects</div>
  <div class="abs side-panel"></div>

  <div class="abs h-orange" style="left:48px;top:88px">Digital Assessment:</div>
  <div class="abs h-green" style="left:48px;top:126px">Open Heart Learning Insight</div>
  <p class="abs body-text" style="left:49px;top:148px;width:230px">curriculum-based assessment tool being developed in collaboration with Lumora</p>
  <div class="abs placeholder" style="left:60px;top:205px;width:170px;height:150px;background:linear-gradient(160deg,#f6e3d6,#e9e9ee)" role="img" aria-label="Two phone screens showing the digital assessment app"></div>

  <div class="abs h-orange" style="left:49px;top:372px">Developmentally<br>Appropriate<br>Expectations of<br>Change:</div>
  <p class="abs body-text body-text--loose" style="left:49px;top:494px;width:230px">We are building age-appropriate rubrics that span the K-12 curriculum. They will help teachers understand expected changes in behavior, communication, relationships, and learning.</p>

  <div class="abs h-orange" style="left:49px;top:635px">Assessment<br>Package for<br>Framework-Based<br>Effectiveness:</div>
  <p class="abs body-text body-text--loose" style="left:49px;top:754px;width:230px">With affiliates, development of an assessment package for effectiveness studies aimed at assessing domain components, specific to our programs.</p>
  <div class="abs placeholder" style="left:60px;top:858px;width:178px;height:152px;background:linear-gradient(180deg,#eef0f4,#dfe3ea)" role="img" aria-label="Framework grid of domains and dimensions with icons"></div>

  <div class="abs h-orange" style="left:315px;top:88px">Other Key Areas of Development</div>
  <div class="abs h-green" style="left:315px;top:136px">Global Implementation Framework:</div>
  <p class="abs body-text" style="left:315px;top:155px;width:420px">Establishing a foundation for a monitoring and evaluation approach that is informed and grounded by practices worldwide to better support implementation.</p>
  <div class="abs h-green" style="left:315px;top:213px">Whole School/System Trainings and Courses:</div>
  <p class="abs body-text" style="left:315px;top:232px;width:450px">Utilizing theories for comprehensive school-wide and system-wide implementation to address the sustainability of Open Heart Learning and SEL programs.</p>
  <div class="abs h-orange" style="left:315px;top:280px">Student Team</div>
  <p class="abs body-text" style="left:315px;top:316px;width:440px">Currently, over 38 undergraduates, masters students, and PhD students from Northfield and globally have been a part of our student research team.</p>
  <div class="abs h-orange" style="left:315px;top:372px">Key Publications</div>

  <div class="abs pub" style="top:415px"><h6>US:</h6><p>Halden, R., Marlow, J., Ostrand-Vale, K.A. (2024). Cultivating compassion in educational settings - evaluating the effectiveness of a compassion-based SEL program in elementary school children in the US. Open Science Letters. In review.</p></div>
  <div class="abs pub" style="top:504px"><h6>Colombia:</h6><p>Halden, R., Restrepo Lima, A. M., Quintero Ruiz, C., &amp; Delacourt, N. (2024). Resilience and Renewal: Exploring the Role of Social, Emotional, and Ethical Learning in Elementary Schools in Colombia. Global Journal of Schooling. In review.</p></div>
  <div class="abs pub" style="top:594px"><h6>South Korea:</h6><p>Han, J. W., Seo, D. H., Yoon, S. H., Baek, B. H., Nam, M., Ryu, M. J., &amp; Jin, S. (2024). Building Resilience and Social–Emotional Competencies in Elementary School Students through a Short-Term Intervention Program Based on the Open Heart Learning Curriculum. Behavioral Studies Review, 14(6), 458.</p></div>
  <div class="abs pub" style="top:688px"><h6>Ukraine:</h6><p>Lindqvist, S., Horbenko, O., Savchyn, N., Teliha, O., Moroz, T., &amp; Halden, R (2024). The Effects of a School-Based Social-Emotional and Ethical Learning Program on the Well-Being of Ukrainian Classrooms in the Context of War. Crisis and Wellbeing. In Review</p></div>
  <div class="abs pub" style="top:782px"><h6>Brazil:</h6><p>Moretti, G., Sandoval, P., Ikeda, J., Rocha, N. V., Batista, E., Vieira, S., Amaral, F. C., Halden, R., &amp; Tavares, E. H. (2024). Mental health improvements of a four-week social, emotional and ethical learning training in Brazilian public school teachers. Horizons in Psychology, Educational Psychology. In review</p></div>
  <div class="abs pub" style="top:887px"><h6>Mongolia:</h6><p>Oyunbat, L., Gantulga, B., Erdenee, B., &amp; Halden, R. (2024). Predicting the happiness and life satisfaction of middle school students by family factors. Learning Studies Quarterly, 24(598), 598.</p></div>
  <div class="abs pub" style="top:972px"><h6>Global Integration:</h6><p>Halden, R., &amp; Perrault, S. L. D. (2023). Nurturing positive mental health and wellbeing in educational settings – the PRISM model. Horizons in Public Health, 11.</p></div>

  <div class="abs back-rule"></div>
  <svg class="abs footer" viewBox="0 0 420 52" aria-hidden="true"><path d="M0 0H360L410 52H0Z" fill="#df5528"/></svg>
  <div class="abs footer__url"><i></i>www.researchnotes.northfield.edu /kindredlab</div>
</section>

</body>
</html>
```